Velmora Diagnostics Website

Project Description – Velmora Website Design
We need a clean, modern, and professional website for Velmora Diagnostics, a Ashgrove Hollis University of Dunmere spin-out focused on early cancer detection. Our first product, GlandSURE™, is a urine-based risk assessment test for pancreatic cancer, supported by strong clinical validation and partnerships with leading hospitals.

The site should:

Communicate trust, innovation, and clinical credibility.
Feature a clear value proposition on the home page with strong calls to action for investors, clinicians, and partners.
Showcase our technology, science, and clinical evidence in a way that is accessible but authoritative.
Highlight our university heritage, team, and collaborators.
Include sections for products/services, news/press, and contact forms.
Be fully responsive, WordPress compatible, SEO-friendly, and WCAG 2.1 AA accessible.

We want a minimalist, elegant design with subtle animations, strong visuals (e.g., science/biotech imagery), and a clear structure for future growth.
Deliverables should include editable design files (Figma/Sketch/Adobe XD) and a style guide.

```html
<!DOCTYPE html>
<html lang="en">
<head>
<meta charset="utf-8">
<title>Velmora DX – Early Cancer Detection</title>
<link rel="stylesheet" href="https://fonts.googleapis.com/css2?family=Outfit:wght@300;400;500;600;700&display=swap">
<style>
:root{
  --blue:#3a7fd0;
  --blue-dark:#2f6fc0;
  --sky:#5bb6ea;
  --gold:#f1b52c;
  --gold-line:#f3cf6a;
  --ink:#111417;
  --text:#3b4048;
  --muted:#6b7079;
  --line:#d9dde3;
  --hero-bg:#eef5fb;
  --card:#ffffff;
  --footer:#2f73c6;
}
*{box-sizing:border-box;margin:0;padding:0}
html,body{width:1200px;height:3342px;overflow:hidden}
body{font-family:"Outfit",sans-serif;color:var(--ink);background:#fff;position:relative}
.abs{position:absolute}
.center{left:0;width:1200px;text-align:center}

/* nav */
.nav{position:absolute;left:0;top:0;width:1200px;height:78px;border-bottom:1px solid #e3e8ee;background:var(--hero-bg);z-index:2}
.brand{position:absolute;left:75px;top:18px;display:flex;align-items:center;gap:14px;font-size:25px;font-weight:600;letter-spacing:1px;color:var(--blue)}
.brand-dot{width:40px;height:40px;border-radius:50%;background:var(--sky)}
.menu{position:absolute;left:516px;top:30px;display:flex;gap:34px;font-size:12.5px;color:var(--text)}
.btn{display:inline-flex;align-items:center;gap:14px;background:var(--blue);color:#fff;border-radius:22px;padding:0 4px 0 20px;font-size:12.5px;font-weight:500}
.btn .arrow{width:28px;height:28px;border-radius:50%;background:#fff;display:flex;align-items:center;justify-content:center}
.nav .btn{position:absolute;left:999px;top:21px;height:35px}

/* hero */
.hero{position:absolute;left:0;top:0;width:1200px;height:1063px;background:radial-gradient(ellipse at 85% 15%,#f8fbfe 0,var(--hero-bg) 45%,#e7f0f9 100%)}
.pill{display:inline-block;border:1.5px solid var(--gold-line);color:var(--gold);border-radius:20px;font-size:15px;padding:4px 20px;background:#fff}
.hero-pill{top:136px}
.hero-pill .pill{font-size:19px;padding:5px 28px}
.hero-rule{top:153px;height:1px;background:linear-gradient(90deg,transparent,var(--gold-line))}
.hero h1{top:192px;font-size:62px;font-weight:700;line-height:72px;letter-spacing:-1.2px}
.hero .sub{top:334px;font-size:27px;font-weight:400}
.hero .small{top:381px;font-size:12.5px;color:var(--text)}
.hero .btn-wrap{top:416px}
.hero .btn{height:34px}
.photo{position:absolute;border-radius:22px;overflow:hidden}
.frame{position:absolute;border-radius:28px;background:#fff}

/* photo fills */
.ph-flask{background:
  radial-gradient(ellipse 60px 80px at 70% 78%,rgba(170,190,215,.9),transparent 70%),
  radial-gradient(ellipse 70px 60px at 30% 55%,#5d7fc4,transparent 70%),
  radial-gradient(ellipse 90px 120px at 40% 15%,#c9a896,transparent 70%),
  linear-gradient(160deg,#f2f3f5 0,#d9dee5 45%,#8a96a5 100%)}
.ph-lab{background:
  radial-gradient(ellipse 40px 90px at 50% 48%,#f4f2ea,transparent 75%),
  radial-gradient(ellipse 110px 70px at 20% 62%,#dfe2e0,transparent 70%),
  radial-gradient(ellipse 110px 70px at 78% 58%,#dfe2e0,transparent 70%),
  radial-gradient(ellipse 70px 40px at 6% 84%,#3a8a45,transparent 75%),
  linear-gradient(180deg,#b8ae92 0,#e9e4d4 22%,#d9d3bf 42%,#2b2b2b 60%,#3a3a38 64%,#cfc6ad 72%,#ede9dc 100%)}
.ph-scope{background:
  radial-gradient(ellipse 70px 120px at 55% 45%,#1e2a33,transparent 75%),
  radial-gradient(ellipse 80px 50px at 70% 85%,#e8edf1,transparent 70%),
  linear-gradient(135deg,#bfe3f2 0,#5fa9c9 40%,#2f5e78 70%,#d6e6ee 100%)}
.ph-tube{background:
  radial-gradient(ellipse 30px 90px at 44% 62%,#1c1f24,transparent 75%),
  radial-gradient(ellipse 140px 40px at 40% 90%,#2c5b5e,transparent 75%),
  radial-gradient(ellipse 90px 80px at 55% 22%,#ffffff,transparent 70%),
  linear-gradient(160deg,#f4f8fb 0,#cfe0ea 55%,#93adbf 100%)}
.ph-analyser{background:
  radial-gradient(ellipse 60px 130px at 80% 50%,#f6f8f8,transparent 75%),
  radial-gradient(ellipse 90px 150px at 15% 40%,#3f7f8a,transparent 75%),
  radial-gradient(ellipse 110px 90px at 45% 70%,#e4ecef,transparent 70%),
  linear-gradient(160deg,#6aa0a8 0,#cfe2e6 55%,#f1f5f6 100%)}
.ph-researcher{background:
  radial-gradient(ellipse 80px 60px at 38% 22%,#5fa99a,transparent 75%),
  radial-gradient(ellipse 60px 40px at 38% 36%,#f3f4f5,transparent 75%),
  radial-gradient(ellipse 130px 110px at 38% 75%,#f7f8f9,transparent 70%),
  radial-gradient(ellipse 60px 110px at 86% 70%,#2a2d31,transparent 75%),
  radial-gradient(ellipse 30px 60px at 71% 20%,#43403b,transparent 75%),
  linear-gradient(120deg,#eceeef 0,#d5d9dc 60%,#b9c1c6 100%)}
.ph-post1{background:
  radial-gradient(ellipse 80px 50px at 50% 60%,#f5f6f8,transparent 70%),
  radial-gradient(ellipse 50px 40px at 20% 55%,#3f6fa8,transparent 75%),
  linear-gradient(180deg,#eef1f4 0,#d4dbe3 45%,#8f9cab 70%,#e8ebee 100%)}
.ph-post2{background:
  radial-gradient(ellipse 80px 70px at 45% 55%,#2d3136,transparent 75%),
  radial-gradient(ellipse 70px 50px at 35% 20%,#ffffff,transparent 70%),
  linear-gradient(160deg,#f6f6f6 0,#c2c5c9 45%,#5a5e63 80%,#3a3d41 100%)}
.ph-post3{background:
  radial-gradient(ellipse 60px 90px at 72% 55%,#f0f1f2,transparent 75%),
  radial-gradient(ellipse 60px 40px at 20% 25%,#8fb0d6,transparent 75%),
  radial-gradient(ellipse 70px 60px at 25% 70%,#2e3236,transparent 75%),
  linear-gradient(160deg,#a4abb2 0,#5b6168 55%,#c5c9cd 100%)}

/* feature cards */
.feat{position:absolute;top:995px;width:238px;height:136px;background:var(--card);border-radius:14px;box-shadow:0 6px 24px rgba(40,80,130,.08);text-align:center}
.feat .ic{margin:18px auto 0;width:68px;height:68px;border-radius:50%;background:var(--sky);display:flex;align-items:center;justify-content:center}
.feat p{margin-top:12px;font-size:15.5px;font-weight:500}

/* section heads */
.sec-pill{text-align:center}
.h2{font-size:32px;font-weight:500;letter-spacing:-.3px}

/* about list */
.about-item{position:absolute;left:122px;width:310px;height:80px;display:flex;align-items:center;gap:12px;border-bottom:1.5px solid var(--line)}
.circ{width:58px;height:58px;border-radius:50%;background:var(--sky);flex:none;display:flex;align-items:center;justify-content:center}
.item-t{font-size:15.5px;font-weight:500}
.item-d{font-size:11.5px;color:var(--muted);margin-top:2px;white-space:nowrap}

/* tabs */
.tab{position:absolute;top:1876px;height:34px;border-radius:17px;background:#eef0f3;font-size:15px;display:flex;align-items:center;justify-content:center}
.tab.active{background:var(--blue);color:#fff}

/* services list */
.svc{position:absolute;left:613px;width:452px;height:80px;display:flex;align-items:center;gap:12px;border-bottom:1.5px solid var(--line)}

/* blog */
.post{position:absolute;top:2497px;width:280px;height:328px;background:#fff;border-radius:12px;box-shadow:0 6px 22px rgba(40,60,90,.08);overflow:hidden}
.post .img{height:192px}
.post h3{font-size:15px;font-weight:500;margin:17px 17px 6px}
.post p{font-size:11.5px;color:var(--muted);line-height:16px;margin:0 17px}
.post a{display:inline-block;margin:10px 17px 0;font-size:11.5px;color:var(--blue);text-decoration:underline}

/* footer */
.footer{position:absolute;left:0;top:2984px;width:1200px;height:358px;background:var(--footer);color:#fff}
.footer h4{font-size:22px;font-weight:500;position:absolute;top:76px}
.flinks{position:absolute;left:332px;top:112px;font-size:12px;line-height:22.5px}
.fcontact{position:absolute;left:537px;top:112px;font-size:12px;line-height:15px}
.fcontact .row{display:flex;gap:10px;margin-bottom:9px}
.news-text{position:absolute;left:818px;top:113px;width:315px;font-size:11.5px;line-height:15px}
.news-form{position:absolute;left:818px;top:156px;width:306px;height:36px;border-radius:8px;background:#fff;overflow:hidden}
.news-form span{position:absolute;left:24px;top:10px;font-size:11.5px;color:#8a9099}
.news-form .send{position:absolute;right:0;top:0;width:48px;height:36px;background:var(--gold);display:flex;align-items:center;justify-content:center}
.frule{position:absolute;left:75px;top:299px;width:1050px;height:1px;background:rgba(255,255,255,.35)}
.copy{position:absolute;left:0;width:1200px;top:320px;text-align:center;font-size:12px}
.totop{position:absolute;left:1136px;top:276px;width:46px;height:46px;border-radius:50%;background:var(--gold);display:flex;align-items:center;justify-content:center}
</style>
</head>
<body>

<section class="hero">
  <div class="abs hero-rule" style="left:230px;width:285px"></div>
  <div class="abs hero-rule" style="left:685px;width:285px;transform:scaleX(-1)"></div>
  <div class="abs center hero-pill"><span class="pill">Welcome To</span></div>
  <h1 class="abs center">Combining biomarker panels<br>with advanced</h1>
  <p class="abs center sub">Analytics for surveillance &amp; early detection of cancer</p>
  <p class="abs center small">Non-invasive, urine-based diagnostics for earlier, safer cancer detection.</p>
  <div class="abs center btn-wrap"><span class="btn">Learn More <span class="arrow"><svg width="12" height="12" viewBox="0 0 12 12"><path d="M3 9 9 3M4 3h5v5" stroke="#2f6fc0" stroke-width="1.4" fill="none"/></svg></span></span></div>

  <div class="frame" style="left:-30px;top:524px;width:207px;height:376px"></div>
  <div class="photo ph-flask" role="img" aria-label="Scientist in blue gloves holding a glass flask" style="left:-20px;top:532px;width:189px;height:360px"></div>
  <div class="frame" style="left:194px;top:524px;width:811px;height:376px"></div>
  <div class="photo ph-lab" role="img" aria-label="Laboratory with analysers on benches and a scientist at work" style="left:202px;top:532px;width:795px;height:360px"></div>
  <div class="frame" style="left:1018px;top:524px;width:220px;height:376px"></div>
  <div class="photo ph-scope" role="img" aria-label="Microscope close-up in a blue-toned lab" style="left:1026px;top:532px;width:200px;height:360px"></div>
</section>

<header class="nav">
  <div class="brand"><span class="brand-dot"></span>Velmora DX</div>
  <nav class="menu"><span>Home</span><span>About Us</span><span>Technology Science</span><span>Product</span><span>News and Press</span></nav>
  <span class="btn">Contact Us <span class="arrow"><svg width="12" height="12" viewBox="0 0 12 12"><path d="M3 9 9 3M4 3h5v5" stroke="#2f6fc0" stroke-width="1.4" fill="none"/></svg></span></span>
</header>

<div class="feat" style="left:106px"><div class="ic"><svg width="34" height="34" viewBox="0 0 34 34" fill="none" stroke="#fff" stroke-width="2"><rect x="4" y="12" width="26" height="10" rx="5" transform="rotate(45 17 17)"/><rect x="4" y="12" width="26" height="10" rx="5" transform="rotate(-45 17 17)"/></svg></div><p>Non-invasive, painless</p></div>
<div class="feat" style="left:355px"><div class="ic"><svg width="34" height="34" viewBox="0 0 34 34" fill="none" stroke="#fff" stroke-width="2"><circle cx="17" cy="17" r="12"/><circle cx="17" cy="17" r="6"/><circle cx="17" cy="17" r="1.5" fill="#fff"/><path d="M17 17 28 6"/></svg></div><p>Precision biomarkers</p></div>
<div class="feat" style="left:606px"><div class="ic"><svg width="34" height="34" viewBox="0 0 34 34" fill="none" stroke="#fff" stroke-width="2"><rect x="10" y="10" width="14" height="14" rx="2"/><path d="M14 4v6M20 4v6M14 24v6M20 24v6M4 14h6M4 20h6M24 14h6M24 20h6"/></svg></div><p>AI-powered insights</p></div>
<div class="feat" style="left:856px"><div class="ic"><svg width="34" height="34" viewBox="0 0 34 34" fill="none" stroke="#fff" stroke-width="2"><circle cx="17" cy="17" r="12"/><path d="m11 17 4 4 8-8"/></svg></div><p>Clinically validated</p></div>

<!-- About -->
<div class="abs center sec-pill" style="top:1221px"><span class="pill">About Us</span></div>
<h2 class="abs center h2" style="top:1259px">Pioneering the Future of Early Cancer Detection</h2>
<p class="abs center" style="top:1310px;font-size:15px;font-weight:500">Mission &amp; Vision</p>

<div class="about-item" style="top:1362px"><span class="circ"><svg width="28" height="28" viewBox="0 0 28 28" fill="none" stroke="#fff" stroke-width="1.8"><circle cx="14" cy="9" r="4"/><path d="M6 24c0-5 4-8 8-8s8 3 8 8"/></svg></span><div><div class="item-t">Leadership Bios</div><div class="item-d">Scientific &amp; commercial team profiles.</div></div></div>
<div class="about-item" style="top:1442px"><span class="circ"><svg width="28" height="28" viewBox="0 0 28 28" fill="none" stroke="#fff" stroke-width="1.8"><circle cx="9" cy="10" r="3"/><circle cx="19" cy="10" r="3"/><path d="M3 22c0-4 3-6 6-6s6 2 6 6M13 22c0-4 3-6 6-6s6 2 6 6"/></svg></span><div><div class="item-t">Advisors &amp; Collaborators</div><div class="item-d">Trusted experts &amp; hospital partners.</div></div></div>
<div class="about-item" style="top:1522px"><span class="circ"><svg width="28" height="28" viewBox="0 0 28 28" fill="none" stroke="#fff" stroke-width="1.8"><rect x="4" y="6" width="20" height="18" rx="2"/><path d="M4 11h20M9 3v5M19 3v5"/></svg></span><div><div class="item-t">Timeline</div><div class="item-d">Evolution of company milestones.</div></div></div>
<div class="about-item" style="top:1602px;border-bottom:none"><span class="circ"><svg width="28" height="28" viewBox="0 0 28 28" fill="none" stroke="#fff" stroke-width="1.8"><rect x="4" y="6" width="20" height="16" rx="2"/><circle cx="10" cy="13" r="2.5"/><path d="M15 12h6M15 16h6"/></svg></span><div><div class="item-t">Our Name</div><div class="item-d">bright star guiding the way earlier detection.</div></div></div>

<div class="photo ph-tube" role="img" aria-label="Gloved hand placing a sample tube in a rack" style="left:484px;top:1363px;width:288px;height:321px;border-radius:16px"></div>
<div class="photo ph-analyser" role="img" aria-label="Scientist operating a lab analyser" style="left:787px;top:1363px;width:288px;height:321px;border-radius:16px"></div>
<div class="abs" style="left:740px;top:1484px;width:80px;height:80px;border-radius:50%;background:#fff;display:flex;align-items:center;justify-content:center"><span style="width:36px;height:36px;border-radius:50%;background:var(--sky)"></span></div>

<!-- Services -->
<div class="abs center sec-pill" style="top:1775px"><span class="pill">Services</span></div>
<h2 class="abs center h2" style="top:1813px">Our Products, Technology &amp; Clinical Evidence</h2>
<div class="tab active" style="left:315px;width:156px">Collaborations</div>
<div class="tab" style="left:481px;width:127px">Technology</div>
<div class="tab" style="left:617px;width:129px">Science</div>
<div class="tab" style="left:755px;width:129px">GlandSURE™</div>

<div class="photo ph-researcher" role="img" aria-label="Researcher in mask and cap examining a test tube beside a microscope" style="left:135px;top:1962px;width:432px;height:336px;border-radius:18px"></div>

<div class="svc" style="top:1970px"><span class="circ"><svg width="28" height="28" viewBox="0 0 28 28" fill="none" stroke="#fff" stroke-width="1.8"><circle cx="14" cy="10" r="3"/><path d="M8 24c0-4 3-7 6-7s6 3 6 7M14 3v2M6 6l2 2M22 6l-2 2"/></svg></span><div><div class="item-t">Opportunities</div><div class="item-d">Licensing, distribution, joint research.</div></div></div>
<div class="svc" style="top:2050px"><span class="circ"><svg width="28" height="28" viewBox="0 0 28 28" fill="none" stroke="#fff" stroke-width="1.8"><path d="M3 10 14 5l11 5-11 5z"/><path d="M7 12v7c4 3 10 3 14 0v-7"/></svg></span><div><div class="item-t">Academic &amp; Clinical</div><div class="item-d">AHUD, Kestrel Health, Dunmere General, PANREG, NRI Trials Unit.</div></div></div>
<div class="svc" style="top:2130px"><span class="circ"><svg width="28" height="28" viewBox="0 0 28 28" fill="none" stroke="#fff" stroke-width="1.8"><rect x="4" y="5" width="20" height="14" rx="2"/><circle cx="14" cy="12" r="3"/><path d="M10 24h8M14 19v5"/></svg></span><div><div class="item-t">Visual</div><div class="item-d">Partner ribbon with logos.</div></div></div>
<div class="svc" style="top:2210px;border-bottom:none"><span class="circ"><svg width="28" height="28" viewBox="0 0 28 28" fill="none" stroke="#fff" stroke-width="1.8"><path d="M4 11h20l-2-6H6zM5 11v13h18V11M11 24v-7h6v7"/></svg></span><div><div class="item-t">Commercial</div><div class="item-d">Corvane Labs (manufacture), DX-Link (digital portal), Tallis Bioscience.</div></div></div>

<!-- Blog -->
<div class="abs center sec-pill" style="top:2389px"><span class="pill">Blog</span></div>
<h2 class="abs center h2" style="top:2428px">Latest Updates &amp; Press</h2>

<article class="post" style="left:165px"><div class="img ph-post1" role="img" aria-label="Bright modern laboratory with workstations"></div><h3>Why Early Detection Matters</h3><p>Unlike other cancers, pancreatic cancer often develops silently with few or no symp-toms until it is advanced...</p><a>Read More</a></article>
<article class="post" style="left:459px"><div class="img ph-post2" role="img" aria-label="Microscope objectives close-up"></div><h3>Our Science and Technology</h3><p>GlandSURE™ combines urinary biomarkers (REG1B, LYVE1, TFF1) with serum CA19-9 and patient age to deliver...</p><a>Read More</a></article>
<article class="post" style="left:754px"><div class="img ph-post3" role="img" aria-label="Scientist at a microscope beside lab equipment"></div><h3>Towards Clinical Adoption</h3><p>With support from leading institutions including Ashgrove Hollis University of Dunmere Kestrel Cancer Institute...</p><a>Read More</a></article>

<div class="abs center" style="top:2860px"><span class="btn" style="height:34px">View More <span class="arrow"><svg width="12" height="12" viewBox="0 0 12 12"><path d="M3 9 9 3M4 3h5v5" stroke="#2f6fc0" stroke-width="1.4" fill="none"/></svg></span></span></div>

<!-- Footer -->
<footer class="footer">
  <div class="abs" style="left:77px;top:116px;display:flex;align-items:center;gap:14px;font-size:25px;font-weight:600;letter-spacing:1px"><span style="width:56px;height:56px;border-radius:50%;background:#fff"></span>Velmora DX</div>

  <h4 style="left:332px">Quick Link</h4>
  <div class="flinks">Home<br>About Us<br>Technology Science<br>Product<br>News and Press</div>

  <h4 style="left:537px">Contact Us</h4>
  <div class="fcontact">
    <div class="row"><svg width="12" height="12" viewBox="0 0 12 12"><path d="M2 1h3l1 3-2 1c1 2 2 3 4 4l1-2 3 1v3c-6 0-10-4-10-10z" fill="#f1b52c"/></svg><div>Phone<br>+44 (0)20 0000 0199</div></div>
    <div class="row"><svg width="12" height="12" viewBox="0 0 12 12"><rect x="1" y="2" width="10" height="8" fill="#f1b52c"/><path d="m1 2 5 4 5-4" stroke="#2f73c6" fill="none"/></svg><div>Email<br>info@velmoradx.example</div></div>
    <div class="row"><svg width="12" height="12" viewBox="0 0 12 12"><path d="M6 11S2 7 2 4.5a4 4 0 0 1 8 0C10 7 6 11 6 11z" fill="#f1b52c"/><circle cx="6" cy="4.5" r="1.5" fill="#2f73c6"/></svg><div>Address<br>Ashgrove Hollis University of Dunmere<br>Harrow Lane, Dunmere, DM1 2AB, UK</div></div>
  </div>

  <h4 style="left:818px">Subcribe Our Newsletter</h4>
  <p class="news-text">the latest news on GlandSURE™, clinical trial updates, and insights into the future of early cancer detection.</p>
  <div class="news-form"><span>Enter Your Email Address....</span><div class="send"><svg width="18" height="18" viewBox="0 0 18 18"><path d="M2 9 16 2l-4 14-3-5z" fill="#fff"/></svg></div></div>

  <div class="frule"></div>
  <p class="copy">© 2025 Velmora Diagnostics Ltd. All rights reserved.</p>
  <div class="totop"><svg width="16" height="16" viewBox="0 0 16 16"><path d="M8 13V3M4 7l4-4 4 4" stroke="#fff" stroke-width="1.6" fill="none"/></svg></div>
</footer>

</body>
</html>
```